Anzeigengestaltung für Beratungsunternehmen
Zielgruppe
Firmenname: BETRIEBSKOMPASS.ORG | Beratung in den Bereichen: Arbeitssicherheit, Brandschutz und Gefahrgut | Zielgruppe: Unternehmen, die Beratung zu obigen Themen suchen | Meine Qualifikationen: Fachkraft für Arbeitssicherheit, Gefahrgut- und Brandschutzbeauftragter, Sachkundiger nach ChemVerbotsV, Ausbilder für Flurförderzeuge, Krane, Hubarbeitsbühnen und Brandschutzhelfer (auch die Ausbilder-Themen könnten erscheinen/hervorgehoben werden - ich biete dafür Kurse an)
Aufgabenstellung
Es soll für Werbung in Zeitschriften und auch für Werbebanner geeignet sein. Vielleicht in 16:9?! Mal hochkant, mal quer.

```html
<!DOCTYPE html>
<html lang="de">
<head>
<meta charset="utf-8">
<title>BETRIEBSKOMPASS.ORG – Anzeige</title>
<link rel="stylesheet" href="https://fonts.googleapis.com/css2?family=Barlow+Condensed:wght@400;500;600;700&display=swap">
<style>
  :root{
    --blue:#1b5679;
    --red:#b0132b;
    --orange:#ea7106;
    --ink:#1f2328;
    --bg-top:#bcc8d1;
    --bg-bottom:#8d9aa5;
    --stage:#3f4244;
    --white:#ffffff;
  }
  *{margin:0;padding:0;box-sizing:border-box}
  html,body{width:1200px;height:861px;overflow:hidden;background:#fff}
  body{position:relative;font-family:"Barlow Condensed",sans-serif;color:var(--ink)}

  .ad{position:absolute;overflow:hidden;background:linear-gradient(180deg,var(--bg-top) 0%,#aebbc5 55%,var(--bg-bottom) 100%)}
  .ad > *{position:absolute}

  .tabs{display:flex;right:0;top:0}
  .tab{flex:1;display:flex;align-items:center;justify-content:center;color:var(--white);font-weight:600;letter-spacing:.3px}
  .tab--safety{background:var(--blue);clip-path:polygon(0 0,100% 0,100% 100%,14% 100%,0 45%)}
  .tab--fire{background:var(--red)}
  .tab--goods{background:var(--orange)}

  .headline{color:var(--red);font-weight:600;letter-spacing:.4px;white-space:nowrap}
  .brand-seal{display:flex;flex-direction:column;align-items:center;justify-content:center}
  .brand-seal .dot{border-radius:50%;background:var(--red)}
  .brand-seal .name{color:var(--red);font-weight:700;white-space:nowrap}

  .product-photo{background:radial-gradient(ellipse 50% 50% at 50% 50%,#f0c415 0%,#e6c11d 35%,#d9df3e 62%,rgba(205,215,90,.5) 85%,rgba(190,200,205,0) 100%)}
  .subhead{color:var(--blue);font-weight:600;white-space:nowrap}
  .body-copy{font-weight:400;white-space:nowrap}

  .contact{background:var(--white);clip-path:polygon(0 0,93% 0,100% 45%,100% 100%,0 100%)}
  .contact > *{position:absolute}
  .contact .label{color:var(--red);font-weight:600;border-bottom:1.5px solid var(--red)}
  .contact .col{line-height:1.3;font-weight:400;white-space:nowrap}
  .portrait-photo{background:linear-gradient(180deg,#c9b9ad 0%,#a48a78 28%,#1d2a44 45%,#121a2e 100%);border-radius:46% 46% 0 0/28% 28% 0 0}

  /* portrait */
  .ad--portrait{width:585px;height:827px}
  .ad--portrait .tabs{left:11px;height:34px}
  .ad--portrait .tab{font-size:19px}
  .ad--portrait .headline{left:46px;top:70px;font-size:61px;line-height:61px}
  .ad--portrait .brand-seal{left:386px;top:70px;width:163px;height:163px}
  .ad--portrait .brand-seal .dot{width:118px;height:118px;margin-bottom:8px}
  .ad--portrait .brand-seal .name{font-size:17px}
  .ad--portrait .product-photo{left:125px;top:322px;width:410px;height:196px}
  .ad--portrait .subhead{left:46px;top:528px;font-size:15.5px;line-height:17px}
  .ad--portrait .body-copy{left:46px;top:571px;font-size:15.5px;line-height:16.8px}
  .ad--portrait .body-copy .para+.para{margin-top:8px}
  .ad--portrait .contact{left:11px;top:729px;width:562px;height:86px}
  .ad--portrait .contact .label{left:14px;top:10px;width:192px;font-size:15px;padding-bottom:2px}
  .ad--portrait .contact .col{top:36px;font-size:12px}
  .ad--portrait .contact .col--a{left:14px}
  .ad--portrait .contact .col--b{left:102px}
  .ad--portrait .portrait-photo{left:322px;top:583px;width:193px;height:244px}

  /* landscape */
  .ad--landscape{left:615px;top:17px;width:570px;height:402px}
  .ad--landscape .tabs{left:10px;height:26px}
  .ad--landscape .tab{font-size:14px}
  .ad--landscape .headline{left:24px;top:48px;font-size:41px;line-height:43px}
  .ad--landscape .brand-seal{left:431px;top:41px;width:121px;height:121px}
  .ad--landscape .brand-seal .dot{width:86px;height:86px;margin-bottom:6px}
  .ad--landscape .brand-seal .name{font-size:12px}
  .ad--landscape .product-photo{left:238px;top:92px;width:188px;height:186px}
  .ad--landscape .subhead{left:27px;top:247px;font-size:11.5px;line-height:12.5px}
  .ad--landscape .body-copy{left:27px;top:279px;font-size:12px;line-height:13px}
  .ad--landscape .body-copy .para+.para{margin-top:6px}
  .ad--landscape .contact{left:262px;top:323px;width:297px;height:67px}
  .ad--landscape .contact .label{left:9px;top:7px;width:150px;font-size:11px;padding-bottom:2px}
  .ad--landscape .contact .col{top:27px;font-size:8.5px}
  .ad--landscape .contact .col--a{left:9px}
  .ad--landscape .contact .col--b{left:77px}
  .ad--landscape .portrait-photo{left:426px;top:260px;width:104px;height:142px}

  .stage{position:absolute;left:615px;top:433px;width:570px;height:411px;background:var(--stage);overflow:hidden}
  .stage .ad--portrait{left:153px;top:19px;transform:scale(.45);transform-origin:0 0}
</style>
</head>
<body>

<section class="ad ad--portrait" style="left:14px;top:17px">
  <div class="tabs"><div class="tab tab--safety">Arbeitssicherheit</div><div class="tab tab--fire">Brandschutz</div><div class="tab tab--goods">Gefahrgut</div></div>
  <h1 class="headline">Wie viel Risiko<br>kann sich Ihr<br>Unternehmen<br>leisten?</h1>
  <div class="brand-seal"><span class="dot"></span><span class="name">BETRIEBSKOMPASS.ORG</span></div>
  <div class="product-photo" role="img" aria-label="Schutzausrüstung: gelber Helm, Kapselgehörschutz, Schutzbrille, Arbeitshandschuhe und Warnweste"></div>
  <h2 class="subhead">Mit BETRIEBSKOMPASS.ORG reduzieren Sie Unfälle,<br>Kosten und Haftungsrisiken.</h2>
  <div class="body-copy">
    <p class="para">Als Fachkraft für Arbeitssicherheit, Brandschutz-<br>und Gefahrgutbeauftragter biete ich Beratung,<br>Begehungen und praxisnahe Schulungen – von<br>Gabelstapler bis Brandschutzhelfer.</p>
    <p class="para">Sichern Sie sich jetzt Ihr unverbindliches Erst-<br>gespräch – für rechtssicheres und nachhaltiges<br>Unternehmensmanagement.</p>
  </div>
  <div class="contact">
    <div class="label">BETRIEBSKOMPASS.ORG</div>
    <div class="col col--a">Matthias Kern<br>Am Lindenweg 12<br>36100 Talheim</div>
    <div class="col col--b">+49 151 20 48 61 37<br>info@betriebskompass.org<br>www.betriebskompass.org</div>
  </div>
  <div class="portrait-photo" role="img" aria-label="Porträt des Beraters im dunklen Anzug mit Krawatte"></div>
</section>

<section class="ad ad--landscape">
  <div class="tabs"><div class="tab tab--safety">Arbeitssicherheit</div><div class="tab tab--fire">Brandschutz</div><div class="tab tab--goods">Gefahrgut</div></div>
  <h1 class="headline">Wie viel Risiko<br>kann sich Ihr<br>Unternehmen<br>leisten?</h1>
  <div class="brand-seal"><span class="dot"></span><span class="name">BETRIEBSKOMPASS.ORG</span></div>
  <div class="product-photo" role="img" aria-label="Schutzausrüstung: gelber Helm, Kapselgehörschutz, Schutzbrille, Arbeitshandschuhe und Warnweste"></div>
  <h2 class="subhead">Mit BETRIEBSKOMPASS.ORG reduzieren<br>Sie Unfälle, Kosten und Haftungsrisiken.</h2>
  <div class="body-copy">
    <p class="para">Als Fachkraft für Arbeitssicherheit, Brandschutz-<br>und Gefahrgutbeauftragter biete ich Beratung,<br>Begehungen und praxisnahe Schulungen – von<br>Gabelstapler bis Brandschutzhelfer.</p>
    <p class="para">Sichern Sie sich jetzt Ihr unverbindliches Erst-<br>gespräch – für rechtssicheres und nachhaltiges<br>Unternehmensmanagement.</p>
  </div>
  <div class="contact">
    <div class="label">BETRIEBSKOMPASS.ORG</div>
    <div class="col col--a">Matthias Kern<br>Am Lindenweg 12<br>36100 Talheim</div>
    <div class="col col--b">+49 151 20 48 61 37<br>info@betriebskompass.org<br>www.betriebskompass.org</div>
  </div>
  <div class="portrait-photo" role="img" aria-label="Porträt des Beraters im dunklen Anzug mit Krawatte"></div>
</section>

<div class="stage">
  <section class="ad ad--portrait">
    <div class="tabs"><div class="tab tab--safety">Arbeitssicherheit</div><div class="tab tab--fire">Brandschutz</div><div class="tab tab--goods">Gefahrgut</div></div>
    <h1 class="headline">Wie viel Risiko<br>kann sich Ihr<br>Unternehmen<br>leisten?</h1>
    <div class="brand-seal"><span class="dot"></span><span class="name">BETRIEBSKOMPASS.ORG</span></div>
    <div class="product-photo" role="img" aria-label="Schutzausrüstung: gelber Helm, Kapselgehörschutz, Schutzbrille, Arbeitshandschuhe und Warnweste"></div>
    <h2 class="subhead">Mit BETRIEBSKOMPASS.ORG reduzieren Sie Unfälle,<br>Kosten und Haftungsrisiken.</h2>
    <div class="body-copy">
      <p class="para">Als Fachkraft für Arbeitssicherheit, Brandschutz-<br>und Gefahrgutbeauftragter biete ich Beratung,<br>Begehungen und praxisnahe Schulungen – von<br>Gabelstapler bis Brandschutzhelfer.</p>
      <p class="para">Sichern Sie sich jetzt Ihr unverbindliches Erst-<br>gespräch – für rechtssicheres und nachhaltiges<br>Unternehmensmanagement.</p>
    </div>
    <div class="contact">
      <div class="label">BETRIEBSKOMPASS.ORG</div>
      <div class="col col--a">Matthias Kern<br>Am Lindenweg 12<br>36100 Talheim</div>
      <div class="col col--b">+49 151 20 48 61 37<br>info@betriebskompass.org<br>www.betriebskompass.org</div>
    </div>
    <div class="portrait-photo" role="img" aria-label="Porträt des Beraters im dunklen Anzug mit Krawatte"></div>
  </section>
</div>

</body>
</html>
```